Revamp our software development company Wix site

We need to rework our Wix website theming, layout, design to match our logo file color and theming. There are a few elements we want to keep, such as the top splash 'typing' header.

The current site is hiketoucan.net. This website I created with Wix, but I never fully finished the copy and all sections.

The feel and mood of the site should be "Warm, professional, inviting, and should project expertise in the field, confidence." But not corporate and cold.

The colors and fonts should match the logo theming. The website must match the logo which was designed in a separate contest. So browns, greens, whites, etc. to create a warm and professional, but fun website.

I want to showcase our app development screenshots in a nice, sharp way.

We are a new company, with only a few clients and projects under our belt. So we don't have lots of need for many testimonials, project showcases, etc. just a couple which is why we went with "Recent work" instead of "Portfolio".

It needs a blog section also that looks great, and will allow me to manage the blog after this project is over. The blog's purpose is for SEO content and marketing.

It will be a huge win for the makerbazaar artist, to make something unique that doesn't look like every other templated website.

We can use the text/sections found on hiketoucan.net, then i would like to tweak some of the copy and sections later.

***This is a Wix website*** I think it would be 2 pages. The landing page, then the blog page.

***Awesome inspiration websites/vibes we like***
https://ninekitesworks.com/
https://vostrella.com/
https://www.larkspinmedia.com/
https://www.triplumeworks.com/
https://harbor-makerhaus.com/
https://frostquill.works/

If you have ideas that need to break free from Wix environment, I am open to that idea also. Wix is just easy for a non-technical founder like me to manage our site/blog.

Thanks!

Target Market(s)

Industry leading commercial and residential construction companies seeking custom software development

Industry/Entity Type

We are a boutique software development studio.

Coding

Coded - Design and coding required

Font styles to use
Sans Serif

Requirements
Must have
• Darker/warm background and overall feel. Relaxed and confident vibes. Simplicity, less is more approach. Blog page. Must have project gallery to showcase high res- screenshots. Clear sans serif fonts, nice contrasting colors.
Nice to have
• If it could have some sort of construction related flare, like photos or icon, that could be good, but it cannot be cheesy. A lot of the stock photos of construction workers etc. are terrible and cheesy (please do not use).
Should not have
• lots of pages, music/sounds, busy theming, tiny fonts

```html
<!DOCTYPE html>
<html lang="en">
<head>
<meta charset="utf-8">
<title>Toucan Studio – Landing Page Mobile View</title>
<link rel="stylesheet" href="https://fonts.googleapis.com/css2?family=Inter:wght@400;500;600;700&family=Montserrat:wght@600&display=swap">
<style>
:root{
  --board:#9c9c9a;
  --ink:#35352f;
  --frame:#35352f;
  --cream:#fdfcee;
  --lime:#b5cc2e;
  --lime-soft:#d9e68a;
  --olive:#8b9461;
  --white:#ffffff;
  --field:#ffffff;
  --muted:#c9c9c4;
}
*{box-sizing:border-box;margin:0;padding:0}
html,body{width:1200px;height:1200px;overflow:hidden}
body{background:var(--board);font-family:"Inter",Arial,sans-serif;color:var(--ink);position:relative}
.abs{position:absolute}
.brand{left:55px;top:62px;display:flex;align-items:center;gap:14px}
.brand-dot{width:42px;height:42px;border-radius:50%;background:var(--lime)}
.brand-name{font-family:"Montserrat",Arial,sans-serif;font-weight:600;font-size:50px;color:var(--white);letter-spacing:-.5px}
.board-title{left:55px;top:176px;font-size:35px;font-weight:700;color:var(--white)}

.screen{position:absolute;width:210px;border:4px solid var(--frame);border-radius:26px;overflow:hidden;background:var(--cream)}
.screen-1{left:227px;top:426px;height:752px}
.screen-2{left:463px;top:245px;height:933px}
.screen-3{left:698px;top:175px;height:1003px}
.screen-4{left:934px;top:21px;height:1157px}

.dark{background:var(--ink)}
.card{position:absolute;background:var(--white);border-radius:16px;box-shadow:0 2px 6px rgba(0,0,0,.08)}
.step-num{position:absolute;left:16px;top:12px;font-size:23px;font-weight:600;color:var(--lime)}
.step-name{position:absolute;left:53px;top:22px;font-size:10.5px;font-weight:600}
.step-body{position:absolute;left:16px;top:52px;right:14px;font-size:8.1px;line-height:1.2}
.mini-logo{font-family:"Inter",sans-serif;font-weight:600;color:var(--white);display:flex;align-items:center;gap:4px}
.mini-logo i{display:block;border-radius:50%;background:var(--lime)}

.hero-line{left:14px;color:var(--white);font-weight:600}
.hero-accent{color:var(--lime)}
.photo{position:absolute}

.acc-line{left:21px;top:709px;width:1px;height:163px;background:var(--white)}
.acc-dot{left:15px;width:13px;height:13px;border-radius:50%;background:var(--white)}
.acc-dot.active{background:var(--lime)}
.acc-head{left:36px;font-size:10.5px;color:var(--white);font-weight:500}
.acc-head.active{color:var(--lime);font-weight:600}
.acc-chev{left:181px}
.acc-body{left:36px;top:721px;width:158px;font-size:7.9px;line-height:1.22;color:var(--white)}

.badge{position:absolute;background:#8e8e88;opacity:.75}
.section-title{font-size:13px;font-weight:600}
.tag{position:absolute;height:17px;width:40px;border-radius:9px;background:var(--lime-soft);font-size:7.5px;display:flex;align-items:center;justify-content:center}
.blog-title{position:absolute;font-size:8px;font-weight:700;line-height:1.2;text-decoration:underline}

.field{position:absolute;left:13px;width:175px;height:25px;background:var(--field);border-radius:4px;font-size:7px;color:#9a9a95;padding:0 8px;display:flex;align-items:center}
.submit{left:13px;width:61px;height:27px;background:var(--lime);border-radius:0 9px 0 9px;color:var(--white);font-size:8.5px;display:flex;align-items:center;justify-content:center}
.contact-row{left:13px;display:flex;align-items:center;gap:6px;font-size:8.3px;color:var(--white)}
.foot-head{left:17px;font-size:8.5px;font-weight:700;letter-spacing:1.3px;color:var(--white);padding-bottom:4px;border-bottom:1.5px solid var(--lime)}
.foot-link{left:13px;font-size:8.4px;color:var(--white)}
.social{width:12px;height:12px;border-radius:50%;background:var(--white);top:861px}
.nav-square{width:25px;height:25px;background:var(--muted);border-radius:3px;display:flex;align-items:center;justify-content:center}
</style>
</head>
<body>

<div class="abs brand"><span class="brand-dot"></span><span class="brand-name">Toucan Studio</span></div>
<h1 class="abs board-title">Landing Page Mobile View</h1>

<!-- Screen 1: hero and first step -->
<section class="screen screen-1">
  <div class="abs dark" style="left:0;top:0;width:100%;height:479px"></div>
  <div class="abs mini-logo" style="left:30px;top:34px;font-size:12px"><i style="width:8px;height:8px"></i>Toucan</div>
  <svg class="abs" style="left:155px;top:38px" width="14" height="11" viewBox="0 0 14 11"><path d="M0 1h14M0 5.5h14M0 10h14" stroke="var(--lime)" stroke-width="1.6"/></svg>
  <div class="abs hero-line" style="top:92px;font-size:19.5px">Take your</div>
  <div class="abs hero-line hero-accent" style="top:117px;font-size:25px">Client</div>
  <div class="abs hero-line hero-accent" style="top:146px;font-size:25px">Experience<span style="font-weight:400">|</span></div>
  <div class="abs hero-line" style="top:182px;font-size:19.5px">to the next level</div>
  <div class="abs" style="left:0;top:220px;width:100%;height:90px;background:linear-gradient(180deg,rgba(181,204,46,0) 0%,rgba(181,204,46,.12) 60%,rgba(181,204,46,0) 100%)"></div>
  <div class="photo" role="img" aria-label="Team meeting around a table in a brick-walled office" style="left:27px;top:265px;width:182px;height:146px;background:linear-gradient(135deg,#6f6b5f,#8a6f58 45%,#4e4f47);clip-path:polygon(22% 0,100% 0,100% 100%,8% 100%,0 78%)"></div>
  <p class="abs" style="left:14px;top:528px;width:176px;text-align:center;font-size:12.5px;font-weight:600;line-height:1.18">We help leading builders break free from off-the-shelf software.</p>
  <div class="card" style="left:13px;top:594px;width:176px;height:131px">
    <span class="step-num">01</span><span class="step-name">Tailor</span>
    <p class="step-body">Research shows that less than 10% of software features are frequently used, leaving many bells and whistles unclicked. We'll tailor to fit and eliminate this waste.</p>
  </div>
  <div class="card" style="left:13px;top:743px;width:176px;height:40px"></div>
</section>

<!-- Screen 2: steps and about -->
<section class="screen screen-2">
  <div class="card" style="left:13px;top:13px;width:176px;height:131px">
    <span class="step-num">02</span><span class="step-name">Empower</span>
    <p class="step-body">When your team has tailored tools, they'll work happier, faster, and more effectively towards your goal KPI's. We'll help turn spreadsheets, folder sharing, and emails into streamlined workflows.</p>
  </div>
  <div class="card" style="left:13px;top:161px;width:176px;height:131px">
    <span class="step-num">03</span><span class="step-name">Outcompete</span>
    <p class="step-body">Deliver results faster, gain performance insights, and leave a lasting impression on clients. Our mission is to create solutions that raise profitability while making your users and clients prefer you over the competition.</p>
  </div>
  <svg class="abs" style="left:0;top:340px" width="202" height="600" viewBox="0 0 202 600" preserveAspectRatio="none"><path d="M0 38L202 8V600H0Z" fill="var(--ink)"/></svg>
  <div class="photo" role="img" aria-label="Team working on laptops around a wooden table in a bright studio" style="left:13px;top:429px;width:180px;height:208px;background:linear-gradient(160deg,#a48e6c,#7a7460 50%,#4f5248);border-radius:0 60px 90px 0"></div>
  <h2 class="abs" style="left:13px;top:664px;font-size:13.5px;font-weight:600;color:var(--white)">About Us</h2>
  <div class="abs acc-line"></div>
  <span class="abs acc-dot active" style="top:702px"></span>
  <span class="abs acc-head active" style="top:702px">OUR STORY</span>
  <svg class="abs acc-chev" style="top:705px" width="8" height="5" viewBox="0 0 8 5"><path d="M1 4l3-3 3 3" stroke="var(--lime)" fill="none"/></svg>
  <p class="abs acc-body">At Toucan, we believe that technology can help businesses achieve more. That's why we've dedicated ourselves to creating software that truly empowers our clients. Our team is made up of experienced developers and business professionals who understand what it takes to succeed in today's competitive landscape.</p>
  <span class="abs acc-dot" style="top:826px"></span>
  <span class="abs acc-head" style="top:826px">OUR VISION</span>
  <svg class="abs acc-chev" style="top:830px" width="8" height="5" viewBox="0 0 8 5"><path d="M1 1l3 3 3-3" stroke="var(--white)" fill="none"/></svg>
  <span class="abs acc-dot" style="top:864px"></span>
  <span class="abs acc-head" style="top:864px">OUR SOFTWARE</span>
  <svg class="abs acc-chev" style="top:868px" width="8" height="5" viewBox="0 0 8 5"><path d="M1 1l3 3 3-3" stroke="var(--white)" fill="none"/></svg>
</section>

<!-- Screen 3: partners, recent works, blogs -->
<section class="screen screen-3">
  <span class="badge" style="left:22px;top:47px;width:62px;height:20px;border-radius:3px"></span>
  <span class="badge" style="left:129px;top:41px;width:34px;height:34px;border-radius:50%"></span>
  <span class="badge" style="left:24px;top:99px;width:62px;height:26px;border-radius:2px"></span>
  <span class="badge" style="left:132px;top:96px;width:30px;height:32px;border-radius:6px"></span>
  <span class="badge" style="left:26px;top:157px;width:56px;height:18px;border-radius:2px"></span>
  <span class="badge" style="left:134px;top:151px;width:30px;height:30px;border-radius:2px"></span>
  <svg class="abs" style="left:0;top:221px" width="202" height="520" viewBox="0 0 202 520" preserveAspectRatio="none"><path d="M0 0H202V476L0 509Z" fill="var(--lime-soft)"/></svg>
  <h2 class="abs section-title" style="left:0;width:202px;text-align:center;top:275px">Our Recent Works</h2>
  <svg class="abs" style="left:84px;top:304px" width="34" height="11" viewBox="0 0 34 11"><path d="M6 1L1.5 5.5 6 10" stroke="#777" stroke-width="1.3" fill="none"/><path d="M27 1l4.5 4.5L27 10" stroke="var(--ink)" stroke-width="1.6" fill="none"/></svg>
  <div class="card" style="left:13px;top:333px;width:176px;height:149px">
    <div class="photo" role="img" aria-label="Dashboard screenshot of the construction ticketing app" style="left:13px;top:38px;width:150px;height:73px;border-radius:6px;background:linear-gradient(180deg,#1f3442,#27495a 60%,#1d2e3a);box-shadow:0 3px 6px rgba(0,0,0,.25)"></div>
    <div class="abs" style="left:0;width:176px;text-align:center;top:128px;font-size:10.5px;font-weight:600">FieldLedger</div>
  </div>
  <div class="abs dark" style="left:13px;top:490px;width:176px;height:149px;border-radius:16px">
    <div class="abs" style="left:0;width:176px;text-align:center;top:40px;font-size:10.5px;font-weight:600;color:var(--white)">Project Title2</div>
    <div class="abs" style="left:50px;top:56px;width:76px;height:1.5px;background:var(--lime)"></div>
    <p class="abs" style="left:8px;width:160px;top:75px;text-align:center;font-size:7px;line-height:1.22;color:var(--white)">Lorem ipsum dolor sit amet consectetur. Augue commodo eu quam sagittis risus magna blandit id lobortis. Amet scelerisque adipiscing id augue sapien a enim. Tincidunt.</p>
  </div>
  <h2 class="abs section-title" style="left:13px;top:782px">Released Blogs</h2>
  <div class="card" style="left:13px;top:812px;width:176px;height:200px;border-radius:16px 16px 0 0;overflow:hidden">
    <div class="photo" role="img" aria-label="Desktop computer, laptop and tablet on a wooden desk" style="left:0;top:0;width:176px;height:120px;background:linear-gradient(150deg,#5d5850,#9c8f80 50%,#6a5e52)"></div>
    <span class="tag" style="left:18px;top:129px">#tag1</span>
    <span class="tag" style="left:67px;top:129px">#tag2</span>
    <span class="tag" style="left:116px;top:129px">#tag3</span>
    <span class="tag" style="left:165px;top:129px"></span>
    <p class="blog-title" style="left:17px;top:166px;width:145px">Blog Title, Lorem ipsum dolor sit amet consectetur.</p>
  </div>
</section>

<!-- Screen 4: blogs, contact, footer -->
<section class="screen screen-4">
  <div class="card" style="left:13px;top:-20px;width:176px;height:50px">
    <p class="blog-title" style="left:17px;top:22px">amet consectetur.</p>
  </div>
  <div class="card" style="left:13px;top:46px;width:176px;height:204px;overflow:hidden">
    <div class="photo" role="img" aria-label="Overhead view of a desk with monitors, laptop and keyboard" style="left:0;top:0;width:176px;height:120px;background:linear-gradient(160deg,#e8e8e4,#c9cdd0 45%,#8a97a5)"></div>
    <span class="tag" style="left:17px;top:129px">#tag1</span>
    <span class="tag" style="left:66px;top:129px">#tag2</span>
    <span class="tag" style="left:115px;top:129px">#tag3</span>
    <span class="tag" style="left:164px;top:129px"></span>
    <p class="blog-title" style="left:17px;top:163px;width:145px;text-decoration:none">Blog Title, Lorem ipsum dolor sit amet consectetur.</p>
  </div>
  <div class="abs nav-square" style="left:70px;top:267px"><svg width="8" height="12" viewBox="0 0 8 12"><path d="M6.5 1L1.5 6l5 5" stroke="#fff" stroke-width="1.8" fill="none"/></svg></div>
  <div class="abs nav-square" style="left:104px;top:267px"><svg width="8" height="12" viewBox="0 0 8 12"><path d="M1.5 1l5 5-5 5" stroke="#fff" stroke-width="1.8" fill="none"/></svg></div>

  <div class="abs dark" style="left:0;top:364px;width:100%;height:800px"></div>
  <h2 class="abs" style="left:13px;top:418px;font-size:13px;font-weight:600;color:var(--white)">Ready to talk?</h2>
  <p class="abs" style="left:13px;top:453px;width:175px;font-size:7.9px;line-height:1.2;color:var(--white)">You can share some quick info by this form and we'll reach out. You can also contact us directly via:</p>
  <div class="abs contact-row" style="top:491px"><svg width="10" height="8" viewBox="0 0 10 8"><rect width="10" height="8" rx="1" fill="#fff"/><path d="M0.5 1l4.5 3.5L9.5 1" stroke="var(--ink)" fill="none"/></svg>dana@hiketoucan.net</div>
  <div class="abs contact-row" style="top:512px"><svg width="10" height="10" viewBox="0 0 24 24"><path d="M6.6 10.8a15 15 0 006.6 6.6l2.2-2.2a1 1 0 011-.25 11.4 11.4 0 003.6.57 1 1 0 011 1V20a1 1 0 01-1 1A17 17 0 013 4a1 1 0 011-1h3.5a1 1 0 011 1 11.4 11.4 0 00.57 3.6 1 1 0 01-.25 1z" fill="#fff"/></svg>555.014.2290</div>
  <div class="field" style="top:539px">Name</div>
  <div class="field" style="top:569px">Type of work interested with</div>
  <div class="field" style="top:599px">Email</div>
  <div class="field" style="top:629px">Phone</div>
  <div class="abs submit" style="top:661px">Submit</div>

  <svg class="abs" style="left:0;top:742px" width="202" height="420" viewBox="0 0 202 420" preserveAspectRatio="none"><path d="M0 32L202 0V420H0Z" fill="var(--olive)"/></svg>
  <div class="abs mini-logo" style="left:13px;top:813px;font-size:19px"><i style="width:12px;height:12px"></i>Toucan</div>
  <span class="abs social" style="left:13px"></span>
  <span class="abs social" style="left:35px"></span>
  <span class="abs social" style="left:57px"></span>
  <div class="abs foot-head" style="top:893px">NAVIGATION</div>
  <span class="abs foot-link" style="top:916px">Home</span>
  <span class="abs foot-link" style="top:934px">What We Do</span>
  <span class="abs foot-link" style="top:953px">Abous Us</span>
  <span class="abs foot-link" style="top:971px">Latest Work</span>
  <span class="abs foot-link" style="top:989px">Blog</span>
  <span class="abs foot-link" style="top:1007px">Contact</span>
  <div class="abs foot-head" style="top:1040px">INFORMATION</div>
  <div class="abs contact-row" style="top:1067px"><svg width="9" height="7" viewBox="0 0 10 8"><rect width="10" height="8" rx="1" fill="#fff"/><path d="M0.5 1l4.5 3.5L9.5 1" stroke="var(--olive)" fill="none"/></svg>dana@hiketoucan.net</div>
  <div class="abs contact-row" style="top:1086px"><svg width="9" height="9" viewBox="0 0 24 24"><path d="M6.6 10.8a15 15 0 006.6 6.6l2.2-2.2a1 1 0 011-.25 11.4 11.4 0 003.6.57 1 1 0 011 1V20a1 1 0 01-1 1A17 17 0 013 4a1 1 0 011-1h3.5a1 1 0 011 1 11.4 11.4 0 00.57 3.6 1 1 0 01-.25 1z" fill="#fff"/></svg>555-014-2290</div>
  <div class="abs contact-row" style="top:1105px;align-items:flex-start"><svg width="9" height="11" viewBox="0 0 24 30"><path d="M12 0a10 10 0 0110 10c0 7.5-10 20-10 20S2 17.5 2 10A10 10 0 0112 0zm0 6a4 4 0 100 8 4 4 0 000-8z" fill="#fff"/></svg><span style="line-height:1.2">1820 Cedar Hollow Ln.<br>Denton, TX 76201</span></div>
</section>

</body>
</html>
```